A landing page for a market leader in France

Our start-up represents a network of professional trainers both independent and working for training organizations. Above all our mission consists of managing administrative and legal procedures necessary to become a training organization. Secondly, our job envisages the obtaining of public financing (subsidies) for customers of our members who wish to receive professional training by fully dealing with the necessary administrative steps. We are providing you with a full presentation of our market, company, services and our particular expectations from the landing page. Briefly: http://www.velmora-trainers.example/pro/home https://www.velmora-trainers.example/pro/tariffs membership https: //www.velmora-trainers. example / pro / rates-management The landing page must contain the following elements: Presentation of the VLMTR and our added value. What do we expect from our landing page? We have a new page of our landing page to a one-page web site with many sections to present the added value of our service, the pricing and the differences between our types of subscription. The landing page has been condensed to a more generalized version of our web-site but clearer, with fewer fields, more information, and more. It also requires reinsurance with customer reviews or cases: https://www.videohost-sample.example/channel/UCzQwXkLmNoPaRsTuVbYdEfGh/videos Graphic design - we prefer to keep your current charter. Please find attached our logo as we are different graphic elements (the main color code: RGB: 08133B). The landing page must be available in a mobile version. Our services 1. Membership To join VLMTR To join the VLMTR you have to pay a membership that is valid for life. The amount of membership varies depending on whether or not it is one of several. Depending on your membership VLMTR can manage all the administrative procedures needed to launch your activity - a so-called "activity declaration". The membership includes activity launching support, pedagogical support, one or more training courses of the trainer, as well as licenses to use our management software. Membership can be paid in 1 to 12 installments (the shorter the payment, the lower the fee). Membership can be paid in 1 to 12 installments (the quicker payment, the lower the fee). The membership is explained on our web-site (eventually, the designer will compete for your current site: https://www.velmora-trainers.example/pro/tarifs-adhesion) 2. Each VLMTR member who benefits from the management of their trainees. We offer 4 options to manage the training and the possible funding: A. The member wants to manage the funding himself: he uses a documentary pack provided. The documents are in accordance with the expectations of financing mechanisms. This option is free and unlimited but does not consider any support. It's autonomous management. B. The member wants to make the compsory documents but it will not be the subject of public subsidy (30 to 50 €). This management is called "Secretariat." C. The member wants to get a handle on the subject of customer satisfaction. This is "Financial managment" D. The member wants to manage the process and optimize the funding: we fully manage the administrative and financial This method is the flagship and premium service of VLMTR that makes it possible for us to finance the customer. subsidies), the cost is equal to 10 and 25% of the amount of the fee. If he does not buy the subscription, the fees will be the highest, while he pays for subscription, it will reduce the fees and give an access to complementary services. We offer 3 types of subscription: Free: includes estimates of service for customers of different types of membership, different modes of management listed above, and a complementary cost method. Partner: all the "Free" subscription features with reduced fees, priority matching, unlimited programs validation, possibility to obtain subsidies the possibility of obtaining within the CPF and for job seekers. Partner: all the "Partner" subscription features with dedicated support and reduced management fees. This pricing you will find on our web-site: https://www.velmora-trainers.example/pro/tariffs-management
Target Market(s)
Therefore, most of our customers are future professionals who wish to launch their training activities. But we also target companies that offer a service and want to provide customers with this service (eg I sell Wordpress services and want to learn my customers to use it).
Number of Pages Required
1 page
Font styles to use
Requirements
Must have
- We need to popularize the complexity of the market and make it clear that it's much easier with us!
Nice to have
- Main color theme: RGB: 08133B

```html
<!DOCTYPE html>
<html lang="fr">
<head>
<meta charset="utf-8">
<title>VLMTR — Accompagnement des formateurs</title>
<link rel="stylesheet" href="https://fonts.googleapis.com/css2?family=Lato:wght@400;700;900&display=swap">
<style>
  :root {
    --navy: #08133b;
    --ink: #0b1540;
    --header-start: #07142a;
    --header-end: #0c2447;
    --gold: #b58a45;
    --logo-text: #e6e8ee;
    --page: #ffffff;
  }
  * { box-sizing: border-box; margin: 0; padding: 0; }
  html, body {
    width: 1200px;
    height: 1000px;
    overflow: hidden;
    background: var(--page);
    font-family: "Lato", Arial, sans-serif;
    color: var(--ink);
  }
  .site-header {
    position: relative;
    height: 183px;
    background: linear-gradient(90deg, var(--header-start) 0%, var(--header-end) 100%);
  }
  .header-rule {
    position: absolute;
    left: 65px;
    right: 0;
    top: 103px;
    height: 1px;
    background: var(--gold);
  }
  .brand-name {
    position: absolute;
    left: 80px;
    top: 56px;
    font-size: 44px;
    font-weight: 400;
    line-height: 1;
    letter-spacing: 1px;
    color: var(--logo-text);
    background: var(--header-start);
    padding-right: 10px;
  }
  .network-signature {
    position: absolute;
    left: 204px;
    top: 58px;
    width: 160px;
    height: 66px;
    background: linear-gradient(90deg, rgba(181,138,69,0.28), rgba(181,138,69,0.12));
    border-radius: 4px;
  }
  .content {
    width: 812px;
    margin-left: 194px;
  }
  .intro { padding-top: 113px; }
  .section-title {
    font-size: 48px;
    font-weight: 900;
    line-height: 64px;
    color: var(--navy);
    letter-spacing: -0.3px;
  }
  .lead {
    font-size: 19.5px;
    line-height: 23px;
    margin-top: 32px;
  }
  .complexity { padding-top: 90px; }
  .complexity .section-title { margin-bottom: 32px; }
  .body-text {
    font-size: 19.5px;
    line-height: 23px;
    margin-bottom: 23px;
  }
</style>
</head>
<body>
  <header class="site-header">
    <div class="header-rule"></div>
    <div class="brand-name">vlmtr</div>
    <div class="network-signature" role="img" aria-label="Signature manuscrite « Réseau national »"></div>
  </header>

  <main class="content">
    <section class="intro">
      <h1 class="section-title">Accompagnement des (futurs) formateurs ou organismes de formation</h1>
      <p class="lead">De la création de votre organisme à l’optimisation des financements de vos clients, on s’occupe de tout!</p>
    </section>

    <section class="complexity">
      <h2 class="section-title">Bienvenue dans le secteur le plus complexe de France</h2>
      <p class="body-text">Le labyrinthe de la formation professionnelle n’a plus de secrets pour nos experts et vous?</p>
      <p class="body-text">Déclaration d’activité, Qualidoc, Dirpreva, CPF, BPF, certifications, RNCP, Inventaire, Agence Compétences, OPCA, OPCO… La liste est encore longue! Avec le VLMTR, oubliez tout ça et concentrez-vous sur votre métier!</p>
    </section>
  </main>
</body>
</html>
```